Business Card Design

Quorvel Software Limited develops and sells venue and event management software called Quorvel Stagehand, which is available in the cloud or on-premise. The company was established in 1986. Most of our customers are performing arts venues, museums and festivals. Our existing design is a bit dull. We need to convey that we are both innovative and reliable.
Not all our people show their mobile phone numbers on their cards, so the design needs to work land line and mobile or land line only.

Industry/Entity Type

Software

Contact Information for Business Card

Helen Trasko
Director
Quorvel Software Limited
42B Milbrook Lane, Harrowfield, Wessex, HF4 2DN
Telephone: +44 (0)1632 640913
Mobile: +44 (0)7945 216804
Email: htrasko@quorvel.net
Web: www.quorvel.net

```html
<!DOCTYPE html>
<html lang="en">
<head>
<meta charset="utf-8">
<title>Quorvel Software Limited – Business Card</title>
<link href="https://fonts.googleapis.com/css2?family=Open+Sans:wght@400;600;700&display=swap" rel="stylesheet">
<style>
  :root {
    --backdrop: #eceded;
    --card: #ffffff;
    --navy: #0d3a6b;
    --blue: #0a5ea8;
    --ink: #3a3f47;
    --shadow: rgba(30, 40, 60, 0.12);
  }
  * { box-sizing: border-box; margin: 0; padding: 0; }
  html, body {
    width: 1200px;
    height: 720px;
    overflow: hidden;
    background: var(--backdrop);
    font-family: "Open Sans", Arial, sans-serif;
  }
  .canvas {
    position: relative;
    width: 1200px;
    height: 720px;
  }
  .card {
    position: absolute;
    top: 210px;
    width: 520px;
    height: 300px;
    background: var(--card);
    box-shadow: 0 10px 28px var(--shadow), 0 1px 3px var(--shadow);
  }
  .card--back { left: 50px; }
  .card--front { left: 630px; }

  .brand {
    position: absolute;
    display: flex;
    align-items: center;
    gap: 14px;
  }
  .brand-square {
    width: 34px;
    height: 34px;
    background: var(--blue);
  }
  .brand-name {
    font-weight: 700;
    color: var(--navy);
    letter-spacing: 0.04em;
    line-height: 1;
  }

  /* Back of card */
  .back-brand { left: 44px; top: 176px; }
  .back-brand .brand-name { font-size: 36px; }
  .back-tagline {
    position: absolute;
    right: 36px;
    top: 86px;
    text-align: right;
  }
  .tagline {
    font-size: 14px;
    color: var(--blue);
    line-height: 1.3;
    white-space: nowrap;
  }
  .back-web {
    margin-top: 6px;
    font-size: 14px;
    font-weight: 700;
    color: var(--ink);
    letter-spacing: 0.06em;
  }

  /* Front of card */
  .front-brand { left: 44px; top: 44px; gap: 16px; }
  .front-brand .brand-name { font-size: 44px; }
  .holder {
    position: absolute;
    left: 220px;
    top: 118px;
    width: 290px;
  }
  .holder-name {
    font-size: 19px;
    font-weight: 600;
    color: var(--navy);
    line-height: 1.1;
  }
  .holder-title {
    font-size: 12px;
    color: var(--ink);
    margin-left: 4px;
  }
  .company {
    margin-top: 14px;
    font-size: 12px;
    font-weight: 700;
    color: var(--navy);
  }
  .address {
    font-size: 11.5px;
    color: var(--ink);
    white-space: nowrap;
  }
  .contacts {
    list-style: none;
    margin-top: 10px;
  }
  .contacts li {
    display: flex;
    align-items: center;
    gap: 7px;
    font-size: 12.5px;
    color: var(--ink);
    line-height: 1.35;
  }
  .contacts svg {
    width: 11px;
    height: 11px;
    flex: none;
  }
</style>
</head>
<body>
<main class="canvas">

  <section class="card card--back" aria-label="Card back">
    <div class="back-tagline">
      <p class="tagline">Smart Planning For Stages And Shows</p>
      <p class="back-web">www.quorvel.net</p>
    </div>
    <div class="brand back-brand">
      <span class="brand-square"></span>
      <span class="brand-name">QUORVEL</span>
    </div>
  </section>

  <section class="card card--front" aria-label="Card front">
    <div class="brand front-brand">
      <span class="brand-square"></span>
      <span class="brand-name">QUORVEL</span>
    </div>
    <div class="holder">
      <p class="holder-name">Helen Trasko</p>
      <p class="holder-title">Managing Director</p>
      <p class="company">Quorvel Software Limited</p>
      <p class="address">42B Milbrook Lane, Harrowfield, Wessex, HF4 2DN</p>
      <ul class="contacts">
        <li>
          <svg viewBox="0 0 12 12" aria-hidden="true"><rect x="3" y="0.5" width="6" height="11" rx="1" fill="none" stroke="#3a3f47" stroke-width="1.2"/><rect x="4.3" y="2" width="3.4" height="4" fill="#3a3f47"/></svg>
          +44 (0)7945 216804
        </li>
        <li>
          <svg viewBox="0 0 12 12" aria-hidden="true"><path d="M1 4.5 Q6 1 11 4.5 L9.5 6 L8 5 L8 4 Q6 3.3 4 4 L4 5 L2.5 6 Z" fill="#3a3f47"/><rect x="2.5" y="6.5" width="7" height="4.5" rx="0.8" fill="#3a3f47"/></svg>
          +44 (0)1632 640913
        </li>
        <li>
          <svg viewBox="0 0 12 12" aria-hidden="true"><rect x="0.7" y="2.5" width="10.6" height="7.5" fill="none" stroke="#3a3f47" stroke-width="1"/><path d="M0.7 2.5 L6 7 L11.3 2.5" fill="none" stroke="#3a3f47" stroke-width="1"/></svg>
          htrasko@quorvel.net
        </li>
        <li>
          <svg viewBox="0 0 12 12" aria-hidden="true"><circle cx="6" cy="6" r="5" fill="none" stroke="#3a3f47" stroke-width="1"/><ellipse cx="6" cy="6" rx="2.2" ry="5" fill="none" stroke="#3a3f47" stroke-width="0.8"/><line x1="1" y1="6" x2="11" y2="6" stroke="#3a3f47" stroke-width="0.8"/></svg>
          quorvel.net
        </li>
      </ul>
    </div>
  </section>

</main>
</body>
</html>
```